Vemra. Packaging for mood-boosting energy drink mix. Upbeat and uplifting.

I need a mockup of a pouch package + a stick. I included an image of a Aqua Tarn pouch + stick for reference. I do not have a die line for the pouch, so feel free to just use the same relative dimensions for the pouch and create a rendering. Here are the specifications for the packaging that I need:
1. The logo is included in the uploaded files. Please use the one that says "bright day spark" beneath "vemra." The logo should take up about the top 1/3 to 1/2 of the pouch.
2. The pouch should be mostly white, especially behind the logo, but feel free to explore yellow or orange for the bottom 1/2 to 2/3 of the packaging.
3. In the center of the packaging, below the logo, please have the product name appear, "mood-boosting energy drink mix" similar to where "Fluid Amplifier" is placed.
4. Below that, create an image of a glass with a stick pouring into it like in the Aqua Tarn pouch.
5. Below the glass, in the bottom center of the package, include "16 sticks. Net Wt. 4 oz. (114 g)
6. On the left side, please include callouts, from top to bottom, "energy blend (80mg caffeine, taurine) + happy blend (saffron, st. john's wort, rhodiola).
7. On the right side, please include callouts, from top to bottom, "electrolytes + vitamins + 0g sugar"
8. Somewhere else on the front of the packaging, please include the flavor name "golden berry," perhaps where they do on the aqua tarn pouch.
9. For the stick, use your creativity.
10. There is no back of packaging to design for this project.

Target Market(s)

My target consumer leads a very active lifestyle and cares deeply about health & wellness.

Colors
0094D4
00A9DD
6FCCEA
C7EBF8
E9F6FB
FFC000
F8CF3A
FAE287
FDF2CF
FEFAEE
F0912C
F2A743
F7CA91
FBE8D2
FDF5EE
EE7325
F08F49
F5BC92
FAE3D3
FDF4ED

Requirements
Must have
• My packaging must make people feel good and maybe even smile when they see it. A brand that does this well is Penn. (www.pennvita-example.com)
Nice to have
• I like 60's Mod Design if you need some inspiration. The packaging should also convey a sense of levity. Like you'll float or dance through life after drinking this.

```html
<!DOCTYPE html>
<html lang="en">
<head>
<meta charset="utf-8">
<title>Vemra – Pouch and Stick</title>
<link href="https://fonts.googleapis.com/css2?family=Poppins:wght@400;600;700&display=swap" rel="stylesheet">
<style>
  :root {
    --bg: #e4e4e4;
    --pouch: #f3f1ec;
    --stick: #f7f5f1;
    --orange: #e0682a;
    --gold: #e4a21f;
    --gold-soft: #f2c96a;
    --white: #ffffff;
  }
  * { margin: 0; padding: 0; box-sizing: border-box; }
  html, body { width: 1200px; height: 840px; overflow: hidden; }
  body {
    background: var(--bg);
    font-family: "Poppins", sans-serif;
    position: relative;
  }

  /* Pouch */
  .pouch {
    position: absolute; left: 366px; top: 145px;
    width: 400px; height: 563px;
    background: var(--pouch);
    border-radius: 6px 6px 10px 10px;
    overflow: hidden;
  }
  .pouch__band {
    position: absolute; left: 0; top: 44px; width: 100%; height: 22px;
    background: var(--orange); color: var(--white);
    font-weight: 600; font-size: 15px; line-height: 22px; text-align: center;
  }
  .pouch__zip {
    position: absolute; left: 0; top: 72px; width: 100%; height: 3px;
    background: #dedbd4;
  }
  .flavor-badge {
    position: absolute; left: 294px; top: 92px;
    width: 94px; height: 62px;
    background: var(--gold);
    border-radius: 47px 47px 0 0 / 47px 47px 0 0;
    transform: rotate(22deg);
    color: var(--white); font-weight: 700; font-size: 16px; line-height: 15px;
    text-align: center; padding-top: 16px;
  }
  .brand {
    position: absolute; left: 44px; top: 148px; width: 312px;
    text-align: right;
  }
  .brand__name {
    display: block;
    font-weight: 700; font-size: 92px; line-height: 100px;
    color: var(--orange); letter-spacing: -2px; text-align: center;
  }
  .brand__tagline {
    display: block; margin-top: -4px;
    font-weight: 600; font-size: 18px; line-height: 22px; color: var(--orange);
  }
  .product-name {
    position: absolute; left: 48px; top: 298px; width: 304px; height: 26px;
    background: var(--orange); color: var(--white);
    border-radius: 13px;
    font-weight: 600; font-size: 15px; line-height: 26px; text-align: center;
  }
  .prep-visual {
    position: absolute; left: 99px; top: 337px; width: 202px; height: 82px;
    background: linear-gradient(90deg, #f1c46a, #e9a33a);
    border-radius: 8px; opacity: .85;
  }
  .blends {
    position: absolute; left: 60px; top: 434px; width: 300px;
    display: flex; align-items: center; gap: 6px;
    color: var(--orange);
  }
  .blend__title { font-weight: 700; font-size: 13px; line-height: 14px; }
  .blend__detail { font-size: 9px; line-height: 11px; }
  .blends__plus { font-weight: 700; font-size: 20px; color: var(--gold); }
  .count-tag {
    position: absolute; left: 173px; top: 476px; width: 55px; height: 87px;
    background: var(--gold); color: var(--white); text-align: center;
  }
  .count-tag__qty { font-weight: 700; font-size: 11px; line-height: 12px; padding-top: 8px; }
  .count-tag__weight { font-size: 7px; line-height: 8px; margin-top: 12px; }

  /* Stick */
  .stick {
    position: absolute; left: 821px; top: 258px; width: 80px; height: 439px;
    background: var(--stick);
    border-top: 8px dotted #ffffff;
    border-bottom: 8px dotted #ffffff;
  }
  .stick__face {
    position: absolute; left: 50%; top: 50%;
    width: 423px; height: 80px;
    transform: translate(-50%, -50%) rotate(-90deg);
    display: flex; align-items: center;
  }
  .stick__claims {
    width: 115px; height: 68px; background: var(--orange); color: var(--white);
    font-weight: 600; font-size: 9px; line-height: 11px;
    display: flex; flex-direction: column; justify-content: center; padding-left: 10px;
  }
  .stick__brand { width: 150px; padding-left: 12px; color: var(--orange); }
  .stick__name { font-weight: 700; font-size: 40px; line-height: 40px; letter-spacing: -1px; }
  .stick__tagline { font-weight: 600; font-size: 7px; }
  .stick__pill {
    background: var(--orange); color: var(--white); font-size: 6px; font-weight: 600;
    border-radius: 4px; padding: 1px 6px; margin-top: 3px; display: inline-block;
  }
  .stick__flavor {
    width: 40px; height: 26px; background: var(--gold-soft);
    border-radius: 20px 20px 0 0; color: var(--white);
    font-weight: 700; font-size: 7px; line-height: 7px; text-align: center; padding-top: 7px;
    margin-right: 14px;
  }
  .stick__blends { color: var(--orange); font-size: 6px; line-height: 7px; }
  .stick__blends strong { font-size: 7px; }
</style>
</head>
<body>
  <section class="pouch">
    <div class="pouch__band">electrolytes + vitamins + 0g sugar</div>
    <div class="pouch__zip"></div>
    <div class="flavor-badge">golden<br>berry</div>

    <div class="brand">
      <span class="brand__name">vemra</span>
      <span class="brand__tagline">bright day spark</span>
    </div>

    <div class="product-name">mood-boosting energy drink mix</div>

    <div class="prep-visual" role="img" aria-label="Illustration of a stick pouring powder into a glass, approximately equal to three filling droplets"></div>

    <div class="blends">
      <div class="blend">
        <div class="blend__title">Energy Blend</div>
        <div class="blend__detail">(80mg Caffeine, Taurine)</div>
      </div>
      <div class="blends__plus">+</div>
      <div class="blend">
        <div class="blend__title">Happy Blend</div>
        <div class="blend__detail">(Saffron, St. John's Wort, Rhodiola)</div>
      </div>
    </div>

    <div class="count-tag">
      <div class="count-tag__qty">16<br>STICKS</div>
      <div class="count-tag__weight">Net Wt.<br>4 oz. (114 g)</div>
    </div>
  </section>

  <section class="stick">
    <div class="stick__face">
      <div class="stick__claims">
        <span>electrolytes +</span>
        <span>vitamins +</span>
        <span>0g sugar</span>
      </div>
      <div class="stick__brand">
        <div class="stick__name">vemra</div>
        <div class="stick__tagline">bright day spark</div>
        <div class="stick__pill">mood-boosting energy drink mix</div>
      </div>
      <div class="stick__flavor">golden<br>berry</div>
      <div class="stick__blends">
        <strong>Energy Blend</strong><br>(80mg Caffeine, Taurine)<br>
        <strong>+ Happy Blend</strong><br>(Saffron, St. John's Wort, Rhodiola)
      </div>
    </div>
  </section>
</body>
</html>
```